Brightwave Travel and Tours

Hotel Reservations
Airline Ticketing
Day Tour

My business is a Travel agency. My services are issuing domestic and international tickets. Book room/hotel reservations local/international.
My color preference is apple green/orange/red/blue.
Images of beaches, tickets,luggage.

```html
<!DOCTYPE html>
<html lang="en">
<head>
<meta charset="utf-8">
<title>Brightwave Travel and Tours – Business Card</title>
<link href="https://fonts.googleapis.com/css2?family=Raleway:wght@500;700;800&display=swap" rel="stylesheet">
<style>
  :root {
    --page-bg: #e9ebee;
    --card-bg: #f7f8f9;
    --card-edge: #c9ced3;
    --navy: #1d4a6b;
    --ink: #1f2a33;
    --sky: #8fb4d6;
    --palm: #4f7d3a;
    --sea: #bfdde3;
    --sand: #cdb48a;
    --accent-orange: #f29a1f;
  }
  html, body {
    margin: 0;
    width: 1200px;
    height: 970px;
    overflow: hidden;
    background: var(--page-bg);
  }
  .card {
    position: absolute;
    left: 100px;
    top: 208px;
    width: 1000px;
    height: 554px;
    background: var(--card-bg);
    border: 1.5px solid var(--card-edge);
    border-radius: 26px;
    overflow: hidden;
    font-family: "Raleway", sans-serif;
  }
  .beach-photo {
    position: absolute;
    left: 0;
    top: 89px;
    width: 100%;
    height: 334px;
    background:
      linear-gradient(90deg, rgba(247,248,249,0) 0%, rgba(247,248,249,0) 48%, rgba(247,248,249,0.85) 68%, var(--card-bg) 82%),
      linear-gradient(180deg, var(--sky) 0%, #c6d9ea 38%, var(--palm) 58%, var(--sea) 74%, var(--sand) 100%);
  }
  .brand {
    position: absolute;
    left: 620px;
    top: 150px;
    width: 340px;
    display: flex;
    flex-direction: column;
    align-items: center;
    gap: 18px;
  }
  .brand-dot {
    width: 110px;
    height: 110px;
    border-radius: 50%;
    background: var(--accent-orange);
  }
  .brand-name {
    margin: 0;
    font-weight: 800;
    font-size: 34px;
    line-height: 1.1;
    text-align: center;
    color: var(--navy);
    letter-spacing: 0.5px;
  }
  .services {
    position: absolute;
    left: 48px;
    top: 446px;
    margin: 0;
    font-weight: 700;
    font-size: 26px;
    color: var(--navy);
  }
  .contacts {
    position: absolute;
    left: 48px;
    top: 490px;
    display: flex;
    gap: 26px;
    font-weight: 500;
    font-size: 22px;
    color: var(--ink);
  }
  .contact-item {
    display: flex;
    align-items: center;
    gap: 10px;
  }
  .contact-item svg { width: 20px; height: 20px; fill: var(--ink); }
</style>
</head>
<body>
  <div class="card">
    <div class="beach-photo" role="img" aria-label="Tropical beach with palm trees, sandy shore and calm sea under a blue sky"></div>

    <div class="brand">
      <div class="brand-dot"></div>
      <p class="brand-name">Brightwave<br>Travel and Tours</p>
    </div>

    <p class="services">Hotel Reservations - Airline Ticketing - Day Tour</p>

    <div class="contacts">
      <span class="contact-item">
        <svg viewBox="0 0 24 24" aria-hidden="true"><path d="M6.6 10.8a15.1 15.1 0 0 0 6.6 6.6l2.2-2.2c.3-.3.7-.4 1-.2 1.1.4 2.3.6 3.6.6.6 0 1 .4 1 1V20c0 .6-.4 1-1 1A17 17 0 0 1 3 4c0-.6.4-1 1-1h3.5c.6 0 1 .4 1 1 0 1.3.2 2.5.6 3.6.1.3 0 .7-.2 1z"/></svg>
        555 - 010 - 222
      </span>
      <span class="contact-item">
        <svg viewBox="0 0 24 24" aria-hidden="true"><path d="M2 5h20v14H2z M4 7v.4l8 5 8-5V7z" fill-rule="evenodd"/></svg>
        info@brightwavetravelandtours.com
      </span>
    </div>
  </div>
</body>
</html>
```